Chai Tea Company needs a Tea Packaging Box Design

Tea Packaging
Dimensions of the Tea Packaging Box: Height 13 cm; Width 8.5 cm; Depth 7 cm
Individual Teabag Packet/ Sachet: Width 6.5 cm; Length 8.25 cm
We are looking for a new tea packaging design, for our tea business. The material of the box is cardboard. We are also looking for a design that will be on each individual tea bag sachet/packet that goes into the box. This design will be very similar to what you design for the tea packaging box.
Product Info:
Our tea company is called “Velmora Leaf”. We sell two types of Chai Tea, once called “Velmora Gold” and one called “Velmora Bloom”. The Velmora Gold has caffeine, while the Velmora Bloom is Naturally Caffeine Free. The Velmora Gold has a black tea base, while the Velmora Bloom has a Rooibos tea base. We will need two tea packaging designs, one for each Chai Tea flavour. The designs for both the teas can be similar, but make sure that you can easily distinguish one from the other (example: make them have different colours or pictures). Both the chai teas, come from the same product line.
Tea Packaging Design:
We are looking for high end tea packaging. We produce high quality teas, and we would like to portray this in our tea packaging. Our teas are made with no artificial flavourings, natural flavourings, or preservatives, so we would also like a natural, organic, high quality look to our tea packaging. Our current logo is a llama. It would be great if you could make the current logo more polished and well made. If you feel that the llama is not well suited or you would like to design the llama differently, we are open to your creative ideas.
General Basic Info:
Keep in mind, we will have both English and French writing on the tea packaging. You do not need to worry about the French writing (we will do the translation), just make sure there is room for it. However, if you feel that you are capable and knowledgeable of incorporating both French and English language into the tea packaging that would be of great help and value.
Back of the Box:
- Will have ingredients and brewing instructions. Basic brewing instructions are: “Add hot water to teabag. Steep for 5-7 minutes, depending on strength preferred. Add milk and your choice of sweetener. Enjoy! See inside panel of box for more detailed instructions”. (The basic brewing instructions, can further be polished or written in a more creative or professional manner).
Front of the Box:
- Will have company name, type of tea, little description of the tea
- 18 teabags
- 54 g (1.9 OZ)
- Should state that this is a product of Alberta, Canada.
Side of the Box:
Any creative wording, slogan, or description about the tea, or whatever you feel would be good on the side of the box.
On the inside flap of the side of the box, there will be detailed instructions on how to brew the tea. These will be different from the simplified brewing instructions on the back of the box. I have attached the advanced brewing instructions as a file. These instructions can further be simplified or reduced to make it easier and cleaner for the consumers to read.
Individual Tea Sachets/ Packets
- These will have a matching look and design of the tea box packaging, except on a smaller scale. Each individual sachet will have the company name, type of tea, little description of the tea in the front of the sachet, while the back will contain the ingredients, and basic brewing instructions.
I have attached a few files, with the dimensions, ingredients, detailed brewing directions, and current logo of the business.
If you have any questions, about the design or packaging please let me know. The winning designer will be required to do a few additional tweaks to finalize the product. Thank you for your time and happy designing!

```html
<!DOCTYPE html>
<html lang="en">
<head>
<meta charset="utf-8">
<title>Velmora Leaf – Tea Packaging</title>
<link rel="stylesheet" href="https://fonts.googleapis.com/css2?family=Josefin+Sans:wght@300;400&family=Lobster+Two:ital@0&display=swap">
<style>
  :root {
    --bg: #e9e9ea;
    --paper: #f7f7f5;
    --kraft: #9c7b42;
    --kraft-dark: #7f6231;
    --wine: #3f0d16;
    --wine-dark: #2c0810;
    --rule-gold: #b08f4c;
    --gold-text: #a8884a;
    --blue-ink: #7f9fb0;
    --blue-fill: #a9c3d0;
    --blue-deep: #4f7084;
    --red-ink: #a4343c;
    --red-fill: #c0676b;
    --red-deep: #7e1f27;
    --small-ink: #8a8a86;
  }
  * { margin: 0; padding: 0; box-sizing: border-box; }
  html, body { width: 1200px; height: 1000px; overflow: hidden; }
  body {
    background: var(--bg);
    font-family: "Josefin Sans", sans-serif;
    position: relative;
  }
  .pack {
    position: absolute;
    display: flex;
    box-shadow: 0 6px 18px rgba(0,0,0,0.12);
  }
  .pack--box { width: 340px; height: 520px; top: 420px; }
  .pack--sachet { width: 260px; height: 330px; top: 40px; }
  .col-gold .pack--box { left: 160px; }
  .col-gold .pack--sachet { left: 200px; }
  .col-bloom .pack--box { left: 700px; }
  .col-bloom .pack--sachet { left: 740px; }

  .band { flex: 0 0 44px; }
  .pack--sachet .band { flex-basis: 34px; }
  .gold .band { background: linear-gradient(180deg, var(--kraft), var(--kraft-dark)); }
  .bloom .band { background: linear-gradient(180deg, var(--wine), var(--wine-dark)); }

  .panel {
    flex: 1;
    background: var(--paper);
    display: flex;
    flex-direction: column;
    align-items: center;
    text-align: center;
    padding: 22px 14px 16px;
  }
  .gold { --ink: var(--blue-ink); --fill: var(--blue-fill); --deep: var(--blue-deep); }
  .bloom { --ink: var(--red-ink); --fill: var(--red-fill); --deep: var(--red-deep); }

  .caffeine {
    display: flex; gap: 38px;
    font-size: 9px; letter-spacing: 0.08em;
    color: var(--small-ink); text-transform: uppercase;
  }
  .variety {
    font-family: "Lobster Two", cursive;
    color: var(--ink);
    font-size: 36px; line-height: 1.1; margin: 6px 0 8px;
  }
  .desc {
    font-size: 11.5px; line-height: 1.3; letter-spacing: 0.05em;
    text-transform: uppercase; color: var(--ink);
  }
  .rule { width: 88%; height: 1px; background: var(--rule-gold); margin: 7px 0; }
  .desc-fr {
    font-size: 9.5px; line-height: 1.35; letter-spacing: 0.04em;
    text-transform: uppercase; color: var(--small-ink);
  }
  .emblem {
    width: 150px; height: 160px; margin-top: 18px;
    background: linear-gradient(180deg, var(--fill), var(--ink));
    opacity: 0.85; border-radius: 4px;
  }
  .brand {
    font-size: 24px; letter-spacing: 0.06em; text-transform: uppercase;
    color: var(--deep); margin-top: 10px; font-weight: 400;
  }
  .count { color: var(--gold-text); margin-top: 8px; line-height: 1.15; }
  .count__num { font-size: 30px; font-weight: 300; }
  .count__label { font-size: 14px; letter-spacing: 0.08em; }
  .count__fr, .count__weight { font-size: 9.5px; letter-spacing: 0.08em; }

  .pack--sachet .panel { padding: 16px 10px 12px; }
  .pack--sachet .emblem { width: 92px; height: 96px; margin: 0 0 6px; }
  .pack--sachet .brand { font-size: 17px; margin: 0 0 12px; }
  .pack--sachet .caffeine { font-size: 7px; gap: 26px; }
  .pack--sachet .variety { font-size: 27px; margin: 4px 0 6px; }
  .pack--sachet .desc { font-size: 8.5px; }
  .pack--sachet .rule { margin: 5px 0; }
  .pack--sachet .desc-fr { font-size: 7.5px; }
</style>
</head>
<body>

<section class="col-gold">
  <article class="pack pack--sachet gold">
    <div class="band"></div>
    <div class="panel">
      <div class="emblem" role="img" aria-label="Pale blue llama emblem"></div>
      <div class="brand">Velmora Leaf</div>
      <div class="caffeine"><span>With caffeine</span><span>Avec la caféine</span></div>
      <h2 class="variety">Velmora Gold</h2>
      <p class="desc">An exotic blend of black tea,<br>cardamon, fennel, cloves,<br>ginger and cinnamon</p>
      <div class="rule"></div>
      <p class="desc-fr">Un mélange exotique de thé noir,<br>cardamome, le fenouil, clous de<br>girofle, le gingembre et la cannelle</p>
    </div>
    <div class="band"></div>
  </article>

  <article class="pack pack--box gold">
    <div class="band"></div>
    <div class="panel">
      <div class="caffeine"><span>With caffeine</span><span>Avec la caféine</span></div>
      <h1 class="variety">Velmora Gold</h1>
      <p class="desc">An exotic blend of black tea,<br>cardamon, fennel, cloves,<br>ginger and cinnamon</p>
      <div class="rule"></div>
      <p class="desc-fr">Un mélange exotique de thé noir,<br>cardamome, le fenouil, clous de<br>girofle, le gingembre et la cannelle</p>
      <div class="emblem" role="img" aria-label="Pale blue llama emblem"></div>
      <div class="brand">Velmora Leaf</div>
      <div class="count">
        <div class="count__num">18</div>
        <div class="count__label">TEA BAGS</div>
        <div class="count__fr">SACHETS DE THÉ</div>
        <div class="count__weight">54 G (1.9 OZ)</div>
      </div>
    </div>
    <div class="band"></div>
  </article>
</section>

<section class="col-bloom">
  <article class="pack pack--sachet bloom">
    <div class="band"></div>
    <div class="panel">
      <div class="emblem" role="img" aria-label="Rose red llama emblem"></div>
      <div class="brand">Velmora Leaf</div>
      <div class="caffeine"><span>Caffeine free</span><span>Sans caféine</span></div>
      <h2 class="variety">Velmora Bloom</h2>
      <p class="desc">A rich blend of South African<br>rooibos tea, cardamon, fennel,<br>cloves, ginger and cinnamon</p>
      <div class="rule"></div>
      <p class="desc-fr">Un riche mélange du thé rooibos d'Afrique<br>du Sud, la cardamome, le fenouil, clous de<br>girofle, le gingembre et la cannelle</p>
    </div>
    <div class="band"></div>
  </article>

  <article class="pack pack--box bloom">
    <div class="band"></div>
    <div class="panel">
      <div class="caffeine"><span>Caffeine free</span><span>Sans caféine</span></div>
      <h1 class="variety">Velmora Bloom</h1>
      <p class="desc">A rich blend of South African<br>rooibos tea, cardamon, fennel,<br>cloves, ginger and cinnamon</p>
      <div class="rule"></div>
      <p class="desc-fr">Un riche mélange du thé rooibos d'Afrique<br>du Sud, la cardamome, le fenouil, clous de<br>girofle, le gingembre et la cannelle</p>
      <div class="emblem" role="img" aria-label="Rose red llama emblem"></div>
      <div class="brand">Velmora Leaf</div>
      <div class="count">
        <div class="count__num">18</div>
        <div class="count__label">TEA BAGS</div>
        <div class="count__fr">SACHETS DE THÉ</div>
        <div class="count__weight">54 G (1.9 OZ)</div>
      </div>
    </div>
    <div class="band"></div>
  </article>
</section>

</body>
</html>
```